My website design

It Will be a to-go website for all service requests from the comfort of your home. services ranging from renting an electrician to fix your home electrical issues, DJ for your party, mark-up artist for your wedding and so on. Here are a few websites for inspiration:

https://www.dwellnook.example/
https://www.chorefinch.example/
https://www.pinlatch.example/

Number of Pages Required

5+ page

Requirements
Must have
• User's registration form
pros resgistation form
filling out job request form
quotes sent sent back to job requester from various pros within the same zip code
quote accepted
ability to review pros once jobs are completed

```html
<!DOCTYPE html>
<html lang="en">
<head>
<meta charset="utf-8">
<title>Homvia — Help around the home</title>
<link href="https://fonts.googleapis.com/css2?family=Lato:ital,wght@0,400;0,700;0,900;1,400&display=swap" rel="stylesheet">
<style>
:root{
  --green:#3fb54a;
  --ink:#222a30;
  --text:#555d63;
  --muted:#8a9399;
  --slate:#5d6b79;
  --white:#ffffff;
  --sky:#eef3f7;
  --star:#e5a823;
}
*{box-sizing:border-box;margin:0;padding:0}
html,body{width:1200px;height:4898px;overflow:hidden}
body{font-family:'Lato',sans-serif;color:var(--text);background:var(--white);position:relative}
.page{position:relative;width:1200px;height:4898px;overflow:hidden}
.abs{position:absolute}
section,header,footer{position:absolute;left:0;width:1200px;overflow:hidden}
.btn{position:absolute;background:var(--green);color:var(--white);font-weight:700;border-radius:30px;display:flex;align-items:center;justify-content:center;font-size:15px;text-transform:uppercase;letter-spacing:.3px}
.section-title{position:absolute;left:0;width:1200px;text-align:center;font-size:34px;font-weight:700;color:var(--ink)}
.title-rule{position:absolute;left:565px;width:70px;height:3px;background:#4e5a63}
.photo{position:absolute}

/* header / hero */
.hero{top:0;height:647px;background:linear-gradient(180deg,#eef0f1 0%,#e3e6e8 60%,#d7dadd 100%)}
.brand{position:absolute;left:112px;top:34px;display:flex;align-items:center;gap:16px}
.brand-mark{width:40px;height:40px;background:var(--green)}
.brand-name{font-size:34px;font-weight:700;color:#4a5359}
.call{position:absolute;left:742px;top:18px;display:flex;align-items:center;gap:12px;font-size:16px;color:#3c454b}
.call-icon{width:32px;height:32px;border-radius:50%;background:#4f5b63;display:flex;align-items:center;justify-content:center}
.login{left:993px;top:11px;width:95px;height:40px;font-size:15px}
.nav-rule{position:absolute;left:580px;top:67px;width:508px;height:1px;background:#b9bfc3}
.nav{position:absolute;top:80px;font-size:15px;color:#2a3136;text-transform:uppercase}
.nav.active{color:var(--green)}
.hero-title{position:absolute;left:110px;top:244px;width:600px;font-size:30px;line-height:36px;font-weight:900;color:#1e2529}
.hero-copy{position:absolute;left:112px;top:322px;width:570px;font-size:13px;line-height:25px;color:#333}
.search{position:absolute;left:114px;top:396px;width:542px;height:50px;background:var(--white);border-radius:30px;box-shadow:0 2px 8px rgba(0,0,0,.08)}
.search-field{position:absolute;left:30px;top:16px;font-size:13px;color:#666}
.search-divider{position:absolute;left:310px;top:8px;width:1px;height:34px;background:#ddd}
.search-zip{position:absolute;left:324px;top:14px;display:flex;align-items:center;gap:10px;font-size:16px;font-weight:700;color:#222}
.search-btn{left:413px;top:0;width:129px;height:50px;font-size:15px}

/* projects */
.projects{top:647px;height:1027px}
.card{position:absolute;width:307px;height:332px;border-radius:3px;overflow:hidden}
.card .photo{left:0;top:0;width:307px;height:249px}
.card-band{position:absolute;left:0;top:249px;width:307px;height:83px;background:var(--green);color:var(--white);text-align:center}
.card-band h3{font-size:17px;font-weight:700;margin-top:18px}
.card-band p{font-size:14px;margin-top:8px}
.more{left:487px;top:922px;width:228px;height:42px;font-size:15px;box-shadow:0 2px 6px rgba(0,0,0,.15)}

/* welcome */
.welcome{top:1674px;height:650px;background:linear-gradient(120deg,#6d7c8c,#5a6878 55%,#6c7a87)}
.welcome-title{position:absolute;left:112px;top:118px;font-size:37px;font-weight:700;color:var(--white)}
.welcome-rule{position:absolute;left:112px;top:178px;width:70px;height:3px;background:var(--white)}
.welcome-copy{position:absolute;left:112px;width:460px;font-size:12.5px;line-height:26px;color:var(--white)}
.learn{left:112px;top:465px;width:149px;height:40px}

/* why */
.why{top:2324px;height:586px}
.why-card{position:absolute;top:167px;width:304px;height:340px;border:1px solid #dcdfe2;background:var(--white);box-shadow:0 2px 8px rgba(0,0,0,.06);text-align:center}
.why-icon{position:absolute;left:100px;top:28px;width:104px;height:104px;border-radius:50%;border:3px solid var(--green);background:#4d5e69;display:flex;align-items:center;justify-content:center}
.why-card h3{position:absolute;left:0;top:152px;width:100%;font-size:17px;line-height:26px;font-weight:700;color:#222}
.why-card p{position:absolute;left:18px;top:212px;width:266px;font-size:12.5px;line-height:26px;color:var(--muted)}

/* taskers */
.taskers{top:2910px;height:704px;background:linear-gradient(120deg,#6f7c89,#5b6977 60%,#66737f)}
.taskers .section-title{color:var(--white);top:128px}
.taskers .title-rule{background:var(--white);top:188px}
.tasker{position:absolute;top:224px;width:307px;height:356px;background:var(--white);border-radius:2px}
.avatar{position:absolute;border-radius:50%;border:3px solid var(--green);background:linear-gradient(135deg,#c9b8a8,#7c6d62)}
.tasker .avatar{left:14px;top:34px;width:60px;height:60px}
.tasker-name{position:absolute;left:88px;top:28px;font-size:17px;color:#222}
.tasker-meta{position:absolute;left:88px;font-size:12px;color:#444;display:flex;align-items:center;gap:6px}
.stars{color:var(--star);letter-spacing:1px;font-size:12px}
.skills-label{position:absolute;left:14px;top:136px;font-size:12.5px;color:#444}
.skill{position:absolute;left:14px;width:280px;display:flex;justify-content:space-between;font-size:12.5px;color:var(--muted)}
.skill b{color:var(--green);font-weight:700;font-size:13.5px}
.tasker-rule{position:absolute;left:14px;width:280px;height:1px;background:#e6e8ea}
.fit{position:absolute;left:14px;top:270px;font-size:12.5px;color:#333}
.fit-copy{position:absolute;left:14px;top:292px;width:280px;font-size:12px;line-height:24px;color:var(--muted)}
.arrow{position:absolute;width:38px;height:38px;border-radius:50%;background:var(--green);display:flex;align-items:center;justify-content:center}

/* testimonial */
.testimonial{top:3614px;height:437px}
.quote{position:absolute;left:160px;top:158px;width:880px;text-align:center;font-style:italic;font-size:14.5px;line-height:30px;color:#2d353b}
.quote-name{position:absolute;left:593px;top:306px;font-size:15px;color:#222}

/* app */
.app{top:4051px;height:466px;background:var(--sky)}
.app-title{position:absolute;left:112px;top:105px;font-size:36px;font-weight:700;color:#1e2529}
.app-rule{position:absolute;left:112px;top:157px;width:70px;height:3px;background:#4e5a63}
.app-copy{position:absolute;left:112px;top:173px;width:440px;font-size:12.5px;line-height:22px;color:var(--text)}
.phone-field{position:absolute;left:112px;top:252px;width:448px;height:50px;border-radius:30px;background:var(--white);border:1px solid #dfe4e8}
.phone-field span{position:absolute;left:24px;top:16px;font-size:13px;color:#666}
.submit{left:326px;top:0;width:122px;height:48px}
.store{position:absolute;top:322px;height:36px;border-radius:6px;background:#111;border:1px solid #444}

/* footer */
.footer{top:4517px;height:381px;background:var(--slate)}
.foot-head{position:absolute;top:112px;font-size:15px;font-weight:700;color:var(--white);text-transform:uppercase}
.foot-list{position:absolute;top:140px;list-style:none}
.foot-list li{font-size:12.5px;line-height:33px;color:var(--white);display:flex;align-items:center;gap:8px}
.foot-brand{position:absolute;left:804px;top:110px;display:flex;align-items:center;gap:14px}
.foot-brand .brand-mark{width:38px;height:38px;background:var(--white)}
.foot-brand .brand-name{color:var(--white);font-size:32px}
.social{position:absolute;top:208px;width:36px;height:36px;border-radius:50%;border:1.5px solid var(--white)}
.foot-rule{position:absolute;left:112px;top:325px;width:976px;height:1px;background:#7b8894}
.copyright{position:absolute;left:0;top:346px;width:1200px;text-align:center;font-size:12px;color:var(--white)}
</style>
</head>
<body>
<div class="page">

<!-- HEADER + HERO -->
<header class="hero">
  <div class="photo" role="img" aria-label="Bright kitchen interior with white cabinets, softly blurred" style="left:0;top:0;width:1200px;height:647px;background:linear-gradient(90deg,#f1f2f3 0%,#e6e8ea 45%,#dadddf 100%)"></div>
  <div class="photo" role="img" aria-label="Smiling handyman in a plaid shirt holding a clipboard" style="left:704px;top:86px;width:440px;height:548px;border-radius:200px 200px 0 0;background:linear-gradient(180deg,#c9a58d 0%,#8a7a70 28%,#5a6672 55%,#3e4f5d 100%)"></div>

  <div class="brand"><span class="brand-mark"></span><span class="brand-name">Homvia</span></div>

  <div class="call">
    <span class="call-icon"><svg width="16" height="16" viewBox="0 0 24 24"><path fill="#fff" d="M6.6 10.8a15.1 15.1 0 0 0 6.6 6.6l2.2-2.2c.3-.3.7-.4 1-.2 1.1.4 2.3.6 3.6.6.6 0 1 .4 1 1V20c0 .6-.4 1-1 1A17 17 0 0 1 3 4c0-.6.4-1 1-1h3.5c.6 0 1 .4 1 1 0 1.3.2 2.5.6 3.6.1.3 0 .7-.2 1z"/></svg></span>
    Call Us : (555) 014 2280
  </div>
  <div class="btn login">Login</div>

  <div class="nav active" style="left:580px">Home</div>
  <div class="nav" style="left:667px">About</div>
  <div class="nav" style="left:765px">Services</div>
  <div class="nav" style="left:880px">Our Work</div>
  <div class="nav" style="left:1011px">Contact</div>
  <div class="nav-rule"></div>

  <h1 class="hero-title">HELP AROUND THE HOME, AT YOUR FINGERTIPS</h1>
  <p class="hero-copy">Lorem ipsum dolor sit amet, consectetur adipiscing elit, sed do eiusmod tempor incididunt ut labore et dolore magna aliqua. Quis ipsum suspendisse ultrices gravida.</p>

  <div class="search">
    <span class="search-field">What's on your to-do list?</span>
    <span class="search-divider"></span>
    <span class="search-zip"><svg width="14" height="18" viewBox="0 0 14 18"><path fill="none" stroke="#aaa" stroke-width="1.4" d="M7 17s6-6.2 6-10A6 6 0 0 0 1 7c0 3.8 6 10 6 10z"/><circle cx="7" cy="7" r="2" fill="none" stroke="#aaa" stroke-width="1.4"/></svg>0000</span>
    <div class="btn search-btn">Search</div>
  </div>

  <svg class="abs" style="left:0;top:560px" width="1200" height="87" viewBox="0 0 1200 87">
    <polygon points="0,40 1200,87 0,87" fill="#3fb54a"/>
    <polygon points="0,87 1200,0 1200,87" fill="#ffffff"/>
  </svg>
</header>

<!-- POPULAR PROJECTS -->
<section class="projects">
  <h2 class="section-title" style="top:76px">Popular Projects In Your Area</h2>
  <div class="title-rule" style="top:132px"></div>

  <article class="card" style="left:112px;top:175px">
    <div class="photo" role="img" aria-label="Man assembling a wooden desk on the floor" style="background:linear-gradient(135deg,#d8d4cf,#9c8f84)"></div>
    <div class="card-band"><h3>Assemble a Table/Desk</h3><p>Avg. Project: $55 – $144</p></div>
  </article>
  <article class="card" style="left:445px;top:175px">
    <div class="photo" role="img" aria-label="Technician mounting a TV bracket on a wall" style="background:linear-gradient(135deg,#5d6670,#b9c2ca)"></div>
    <div class="card-band"><h3>Mount a TV or Mirror</h3><p>Avg. Project: $55 – $144</p></div>
  </article>
  <article class="card" style="left:780px;top:175px">
    <div class="photo" role="img" aria-label="Couple carrying moving boxes to a truck" style="background:linear-gradient(135deg,#3f4a55,#b49a78)"></div>
    <div class="card-band"><h3>Move Boxes via Truck</h3><p>Avg. Project: $55 – $144</p></div>
  </article>
  <article class="card" style="left:112px;top:536px">
    <div class="photo" role="img" aria-label="DJ mixing music at a party" style="background:linear-gradient(135deg,#2b2f33,#6c6760)"></div>
    <div class="card-band"><h3>DJ for your party</h3><p>Avg. Project: $55 – $144</p></div>
  </article>
  <article class="card" style="left:445px;top:536px">
    <div class="photo" role="img" aria-label="Make-up artist preparing a client" style="background:linear-gradient(135deg,#8c7465,#d9c2b1)"></div>
    <div class="card-band"><h3>Mark-up artist</h3><p>Avg. Project: $55 – $144</p></div>
  </article>
  <article class="card" style="left:780px;top:536px">
    <div class="photo" role="img" aria-label="Plumber fixing pipes under a sink" style="background:linear-gradient(135deg,#d7dde2,#4a6a8e)"></div>
    <div class="card-band"><h3>Fix a Running Toilet</h3><p>Avg. Project: $55 – $144</p></div>
  </article>

  <div class="btn more">View More Projects</div>
</section>

<!-- WELCOME -->
<section class="welcome">
  <div class="photo" role="img" aria-label="Repairman working on a kitchen cabinet, toned in slate blue" style="left:0;top:0;width:1200px;height:650px;background:linear-gradient(120deg,rgba(120,135,150,.5),rgba(80,95,110,.3))"></div>
  <svg class="abs" style="left:0;top:0" width="1200" height="650" viewBox="0 0 1200 650">
    <polygon points="0,0 1200,0 0,60" fill="#ffffff"/>
    <polygon points="640,40 1200,0 1200,48" fill="#3fb54a"/>
    <polygon points="0,655 0,610 560,600" fill="#3fb54a"/>
    <polygon points="0,650 1200,600 1200,650" fill="#ffffff"/>
  </svg>
  <div class="photo" role="img" aria-label="Smiling couple paying online with a laptop and card" style="left:600px;top:96px;width:500px;height:400px;border-radius:6px;background:linear-gradient(135deg,#c8a990,#8f7769 50%,#6e7c89)"></div>

  <h2 class="welcome-title">Welcome to Homvia</h2>
  <div class="welcome-rule"></div>
  <p class="welcome-copy" style="top:204px">Lorem ipsum dolor sit amet, consectetur adipiscing elit, tempor incididunt ut labore et dolore magna aliqua. Quis ipsum suspendisse ultrices gravida. Risus commodo viverra maecenas accumsan lacus vel facilisis. Lorem im dolor sit amet, consectetur adipiscing elit, sed do eiusmod tincididunt ut labore et dolore magna aliqua.</p>
  <p class="welcome-copy" style="top:358px">Lorem ipsum dolor sit amet, consectetur adipiscing elit, tempor incididunt ut labore et dolore magna aliqua. Quis ipsum suspendisse ultrices gravida. Risus commodo viverra maecenas accumsan lacus vel facilisis.</p>
  <div class="btn learn">Learn More</div>
</section>

<!-- WHY CHOOSE -->
<section class="why">
  <h2 class="section-title" style="top:72px">Why Choose Homvia</h2>
  <div class="title-rule" style="top:130px"></div>

  <article class="why-card" style="left:112px">
    <div class="why-icon"><svg width="54" height="54" viewBox="0 0 54 54" fill="none" stroke="#fff" stroke-width="2"><circle cx="20" cy="9" r="4"/><path d="M20 14v16l-5 14M20 30l5 14M14 20h12"/><rect x="32" y="28" width="12" height="12"/><circle cx="34" cy="45" r="2"/><circle cx="42" cy="45" r="2"/></svg></div>
    <h3>Choose your Tasker by reviews,<br>skills, and price</h3>
    <p>Lorem ipsum dolor sit amet, cotur adipiscing elit, sed do eiusmod tempor indunt ut labore et dolore magna aliqua.s ipsum suspendisse ultrices gravida. Risus commodo</p>
  </article>
  <article class="why-card" style="left:447px">
    <div class="why-icon"><svg width="54" height="54" viewBox="0 0 54 54" fill="none" stroke="#fff" stroke-width="2"><rect x="9" y="12" width="36" height="32" rx="3"/><path d="M9 20h36M17 8v7M37 8v7"/><path d="M15 26h4M23 26h4M31 26h4M15 32h4M23 32h4M31 32h4M15 38h4M23 38h4M31 38h4"/></svg></div>
    <h3>Schedule when it works for you<br>as early as today</h3>
    <p>Lorem ipsum dolor sit amet, cotur adipiscing elit, sed do eiusmod tempor indunt ut labore et dolore magna aliqua.s ipsum suspendisse ultrices gravida. Risus commodo</p>
  </article>
  <article class="why-card" style="left:784px">
    <div class="why-icon"><svg width="54" height="54" viewBox="0 0 54 54" fill="none" stroke="#fff" stroke-width="2"><rect x="8" y="22" width="32" height="20" rx="2"/><path d="M8 28h32M12 36h8"/><path d="M18 22l20-12 8 14-6 4"/></svg></div>
    <h3>Chat, pay, tip, and review all<br>through one platform</h3>
    <p>Lorem ipsum dolor sit amet, cotur adipiscing elit, sed do eiusmod tempor indunt ut labore et dolore magna aliqua.s ipsum suspendisse ultrices gravida. Risus commodo</p>
  </article>
</section>

<!-- FEATURED TASKERS -->
<section class="taskers">
  <div class="photo" role="img" aria-label="Worker fitting a kitchen cabinet, toned in slate blue" style="left:0;top:0;width:1200px;height:704px;background:linear-gradient(120deg,rgba(140,150,160,.35),rgba(70,85,100,.25))"></div>
  <svg class="abs" style="left:0;top:0" width="1200" height="704" viewBox="0 0 1200 704">
    <polygon points="0,0 1200,0 0,30" fill="#ffffff"/>
    <polygon points="680,32 1200,0 1200,38" fill="#3fb54a"/>
    <polygon points="0,704 0,664 600,656" fill="#3fb54a"/>
    <polygon points="0,704 1200,660 1200,704" fill="#ffffff"/>
  </svg>
  <h2 class="section-title">Featured Taskers</h2>
  <div class="title-rule"></div>

  <article class="tasker" style="left:112px">
    <div class="avatar" role="img" aria-label="Portrait of Alexander k."></div>
    <div class="tasker-name">Alexander k.</div>
    <div class="tasker-meta" style="top:56px"><span class="stars">★★★★★</span>100% positive reviews</div>
    <div class="tasker-meta" style="top:80px"><svg width="16" height="16" viewBox="0 0 16 16"><circle cx="8" cy="8" r="7" fill="none" stroke="#3fb54a" stroke-width="1.3"/><path d="M4.5 8.2l2.3 2.3 4.5-4.8" fill="none" stroke="#3fb54a" stroke-width="1.5"/></svg>123 completed tasks</div>
    <div class="tasker-rule" style="top:118px"></div>
    <div class="skills-label">Featured Skills</div>
    <div class="skill" style="top:164px"><span>Shopping</span><b>$49.41/hr</b></div>
    <div class="skill" style="top:192px"><span>Help Moving</span><b>$49.41/hr</b></div>
    <div class="skill" style="top:220px"><span>Home Repairs</span><b>$49.41/hr</b></div>
    <div class="tasker-rule" style="top:254px"></div>
    <div class="fit">I'm the right person for the job:</div>
    <p class="fit-copy">Lorem ipsum dolor sit amet, conetur adipiscing elit, sed do eiusmod tempor incididunt</p>
  </article>
  <article class="tasker" style="left:446px">
    <div class="avatar" role="img" aria-label="Portrait of WilliamJohn"></div>
    <div class="tasker-name">WilliamJohn</div>
    <div class="tasker-meta" style="top:56px"><span class="stars">★★★★★</span>100% positive reviews</div>
    <div class="tasker-meta" style="top:80px"><svg width="16" height="16" viewBox="0 0 16 16"><circle cx="8" cy="8" r="7" fill="none" stroke="#3fb54a" stroke-width="1.3"/><path d="M4.5 8.2l2.3 2.3 4.5-4.8" fill="none" stroke="#3fb54a" stroke-width="1.5"/></svg>123 completed tasks</div>
    <div class="tasker-rule" style="top:118px"></div>
    <div class="skills-label">Featured Skills</div>
    <div class="skill" style="top:164px"><span>Shopping</span><b>$49.41/hr</b></div>
    <div class="skill" style="top:192px"><span>Help Moving</span><b>$49.41/hr</b></div>
    <div class="skill" style="top:220px"><span>Home Repairs</span><b>$49.41/hr</b></div>
    <div class="tasker-rule" style="top:254px"></div>
    <div class="fit">I'm the right person for the job:</div>
    <p class="fit-copy">Lorem ipsum dolor sit amet, conetur adipiscing elit, sed do eiusmod tempor incididunt</p>
  </article>
  <article class="tasker" style="left:781px">
    <div class="avatar" role="img" aria-label="Portrait of Jeffrey C."></div>
    <div class="tasker-name">Jeffrey C.</div>
    <div class="tasker-meta" style="top:56px"><span class="stars">★★★★★</span>100% positive reviews</div>
    <div class="tasker-meta" style="top:80px"><svg width="16" height="16" viewBox="0 0 16 16"><circle cx="8" cy="8" r="7" fill="none" stroke="#3fb54a" stroke-width="1.3"/><path d="M4.5 8.2l2.3 2.3 4.5-4.8" fill="none" stroke="#3fb54a" stroke-width="1.5"/></svg>123 completed tasks</div>
    <div class="tasker-rule" style="top:118px"></div>
    <div class="skills-label">Featured Skills</div>
    <div class="skill" style="top:164px"><span>Shopping</span><b>$49.41/hr</b></div>
    <div class="skill" style="top:192px"><span>Help Moving</span><b>$49.41/hr</b></div>
    <div class="skill" style="top:220px"><span>Home Repairs</span><b>$49.41/hr</b></div>
    <div class="tasker-rule" style="top:254px"></div>
    <div class="fit">I'm the right person for the job:</div>
    <p class="fit-copy">Lorem ipsum dolor sit amet, conetur adipiscing elit, sed do eiusmod tempor incididunt</p>
  </article>

  <div class="arrow" style="left:1100px;top:382px"><svg width="14" height="14" viewBox="0 0 14 14"><path d="M5 2l5 5-5 5" fill="none" stroke="#fff" stroke-width="2"/></svg></div>
</section>

<!-- TESTIMONIAL -->
<section class="testimonial">
  <h2 class="section-title" style="top:68px">Don't Just Take Our Word For It</h2>
  <div class="title-rule" style="top:126px"></div>
  <div class="arrow" style="left:98px;top:186px"><svg width="14" height="14" viewBox="0 0 14 14"><path d="M9 2L4 7l5 5" fill="none" stroke="#fff" stroke-width="2"/></svg></div>
  <p class="quote">Lorem ipsum dolor sit amet, consectetur adipiscing elit, sed do eiusmod tempor incididunt ut labore et dolore magna aliqua. Quis ipsum suspendisse ultrices gravida. Risus commodo viverra maecenas accumsan lacus vel facilisis. Lorem ipsum dolor sit amet, consectetur adipiscing elit, sed do eiusmod tempor incididunt ut labore et dolore magna aliqua.Lorem ipsum dolor sit amet, consectetur adipiscing elit, sed do eiusmod tempor incididunt ut labore et dolore magna aliqua.</p>
  <div class="arrow" style="left:1067px;top:186px"><svg width="14" height="14" viewBox="0 0 14 14"><path d="M5 2l5 5-5 5" fill="none" stroke="#fff" stroke-width="2"/></svg></div>
  <div class="avatar" role="img" aria-label="Portrait of the reviewer" style="left:514px;top:291px;width:64px;height:64px"></div>
  <div class="quote-name">-John smith</div>
  <div class="stars abs" style="left:593px;top:328px">★★★★★</div>
</section>

<!-- APP -->
<section class="app">
  <svg class="abs" style="left:0;top:0" width="1200" height="30" viewBox="0 0 1200 30"><polygon points="0,0 1200,0 0,26" fill="#ffffff"/></svg>
  <div class="photo" role="img" aria-label="Family unpacking moving boxes beside a van" style="left:656px;top:18px;width:544px;height:448px;background:linear-gradient(135deg,#e9eef2 0%,#b7a48e 45%,#4b5560 100%)"></div>
  <h2 class="app-title">Get more done on the go</h2>
  <div class="app-rule"></div>
  <p class="app-copy">Lorem ipsum dolor sit amet, consectetur adipiscing elit, sed do eiusmod tempor incididunt ut labore et dolore magna aliqua. Quis ipsum suspendisse ultrices gravida.</p>
  <div class="phone-field"><span>Enter your mobile number</span><div class="btn submit">Submit</div></div>
  <div class="store" style="left:118px;width:103px"></div>
  <div class="store" style="left:232px;width:118px"></div>
</section>

<!-- FOOTER -->
<footer class="footer">
  <svg class="abs" style="left:0;top:0" width="1200" height="44" viewBox="0 0 1200 44">
    <polygon points="0,0 700,0 0,40" fill="#3fb54a"/>
  </svg>

  <div class="foot-head" style="left:112px">Information</div>
  <ul class="foot-list" style="left:112px"><li>About Us</li><li>Careers</li><li>Press</li><li>Blog</li><li>Terms &amp; Privacy</li></ul>

  <div class="foot-head" style="left:331px">Services</div>
  <ul class="foot-list" style="left:331px"><li>Lorem ipsum dolor sit</li><li>Lorem ipsum dolor sit</li><li>Lorem ipsum dolor sit</li><li>Lorem ipsum dolor sit</li><li style="color:#3fb54a">Sitemap</li></ul>

  <div class="foot-head" style="left:566px">Contact Us</div>
  <ul class="foot-list" style="left:566px">
    <li><svg width="10" height="13" viewBox="0 0 14 18"><path fill="#fff" d="M7 17s6-6.2 6-10A6 6 0 0 0 1 7c0 3.8 6 10 6 10z"/></svg>PO Box 2210 Elmvale</li>
    <li style="padding-left:18px">Your location</li>
    <li><svg width="12" height="10" viewBox="0 0 12 10" fill="none" stroke="#fff"><rect x=".5" y=".5" width="11" height="9"/><path d="M.5 .5l5.5 5 5.5-5"/></svg>hello@homvia.example</li>
    <li><svg width="12" height="12" viewBox="0 0 24 24"><path fill="#fff" d="M6.6 10.8a15.1 15.1 0 0 0 6.6 6.6l2.2-2.2c.3-.3.7-.4 1-.2 1.1.4 2.3.6 3.6.6.6 0 1 .4 1 1V20c0 .6-.4 1-1 1A17 17 0 0 1 3 4c0-.6.4-1 1-1h3.5c.6 0 1 .4 1 1 0 1.3.2 2.5.6 3.6.1.3 0 .7-.2 1z"/></svg>555-014-2280</li>
  </ul>

  <div class="foot-brand"><span class="brand-mark"></span><span class="brand-name">Homvia</span></div>
  <span class="social" style="left:806px"></span>
  <span class="social" style="left:852px"></span>
  <span class="social" style="left:898px"></span>
  <span class="social" style="left:944px"></span>

  <div class="foot-rule"></div>
  <div class="copyright">Copyright © 2020 Homvia. All Rights Reserved.</div>
</footer>

</div>
</body>
</html>
```